Visitenkarten-Design für Goldankauf und Verkauf von Trauringen
Zielgruppe
Goldankauf und Verkauf von Trauringen
Aufgabenstellung
Edel, nicht zu bunt, das Design soll sich dem Kunden einprägen, ansprechend, gerne können auch Wasserzeichen verwendet werden.

```html
<!DOCTYPE html>
<html lang="de">
<head>
<meta charset="utf-8">
<title>Feinglanz – Visitenkarten</title>
<link href="https://fonts.googleapis.com/css2?family=Cinzel:wght@400;500&family=Old+Standard+TT&display=swap" rel="stylesheet">
<style>
  :root{
    --stage-center:#ffffff;
    --stage-edge:#e4e4e4;
    --card-black:#0b0b0b;
    --card-deep:#050505;
    --gold:#d9b44a;
    --gold-light:#fff39a;
    --gold-dark:#8c5a0e;
    --text-light:#f3f0e8;
    --photo-warm:#6b4a33;
    --photo-glow:#c99a5a;
  }
  *{margin:0;padding:0;box-sizing:border-box}
  html,body{width:1200px;height:1200px;overflow:hidden}
  body{
    background:radial-gradient(circle at 50% 50%,var(--stage-center) 0%,var(--stage-edge) 100%);
    position:relative;
    font-family:"Old Standard TT",serif;
  }
  .card{
    position:absolute;left:299px;width:602px;height:390px;
    background:linear-gradient(160deg,#151515 0%,var(--card-black) 50%,var(--card-deep) 100%);
    overflow:hidden;
  }
  .card--front{top:197px}
  .card--back{top:620px}
  .gold-band{
    position:absolute;left:0;right:0;height:11px;
    background:linear-gradient(90deg,var(--gold-light) 0%,#e9cf6c 45%,var(--gold) 70%,var(--gold-dark) 100%);
  }
  .gold-band--top{top:0}
  .gold-band--bottom{bottom:0}

  .portrait{
    position:absolute;top:11px;bottom:11px;right:0;width:320px;
    background:
      radial-gradient(ellipse at 72% 30%,var(--photo-glow) 0%,var(--photo-warm) 30%,transparent 60%),
      radial-gradient(ellipse at 55% 85%,#b8893f 0%,#5a3c1c 30%,transparent 60%),
      linear-gradient(90deg,transparent 0%,rgba(20,14,10,.6) 40%,#2a1d14 100%);
  }

  .brand{position:absolute;left:25px;top:122px}
  .brand__name{
    display:flex;align-items:center;gap:12px;
    font-family:"Cinzel",serif;font-weight:400;font-size:42px;color:var(--gold);
    letter-spacing:1px;
  }
  .brand__dot{width:30px;height:30px;border-radius:50%;background:var(--gold)}
  .brand__rule{width:300px;height:1px;background:var(--gold);margin:4px 0 0 42px}
  .brand__tagline{
    margin:6px 0 0 128px;font-size:17px;color:var(--text-light);
  }
  .front-url{
    position:absolute;left:25px;top:336px;
    font-family:"Cinzel",serif;font-size:14px;color:var(--gold);letter-spacing:.5px;
  }

  .owner{
    position:absolute;left:27px;top:145px;
    font-family:"Cinzel",serif;font-size:30px;color:var(--gold);letter-spacing:-.5px;
  }
  .quick-contact{
    position:absolute;left:27px;top:187px;display:flex;align-items:center;gap:8px;
    font-size:17px;color:var(--text-light);
  }
  .quick-contact svg{width:18px;height:18px;fill:var(--gold)}
  .quick-contact .sep{width:4px}

  .details{
    position:absolute;left:25px;top:324px;display:flex;
    font-size:14px;color:var(--text-light);line-height:21px;
  }
  .details__col{display:grid;grid-template-columns:18px auto;column-gap:2px;align-items:center}
  .details__col--address{width:186px}
  .details__col--web{width:210px}
  .details svg{width:12px;height:12px;fill:var(--gold)}
</style>
</head>
<body>

<section class="card card--front">
  <div class="gold-band gold-band--top"></div>
  <div class="portrait" role="img" aria-label="Porträtfoto einer Frau mit goldglitzernden Lippen und goldenem Spitzenschmuck"></div>
  <div class="brand">
    <div class="brand__name"><span class="brand__dot"></span>Feinglanz</div>
    <div class="brand__rule"></div>
    <div class="brand__tagline">Goldankauf &amp; Trauringe</div>
  </div>
  <div class="front-url">WWW.FEINGLANZ-HANAU.DE</div>
  <div class="gold-band gold-band--bottom"></div>
</section>

<section class="card card--back">
  <div class="gold-band gold-band--top"></div>
  <h1 class="owner">INH. MARA LINDQVIST</h1>
  <div class="quick-contact">
    <svg viewBox="0 0 24 24"><path d="M6.6 2.5l3 4-2 2.5c1.2 2.8 3.5 5.5 6.4 7l2.5-2 4 3-2 4.5C10 21 3 14 2.5 4.5z"/></svg>
    <span>06181-5550142</span>
    <span class="sep"></span>
    <svg viewBox="0 0 24 24"><path d="M2 5h20v14H2z M2 5l10 8 10-8" stroke="#0b0b0b" stroke-width="1.5"/></svg>
    <span>info@feinglanz-hanau.de</span>
  </div>

  <div class="details">
    <div class="details__col details__col--address">
      <svg viewBox="0 0 24 24"><path d="M12 1a8 8 0 0 0-8 8c0 6 8 14 8 14s8-8 8-14a8 8 0 0 0-8-8zm0 11a3 3 0 1 1 0-6 3 3 0 0 1 0 6z"/></svg><span>Lindenallee 12</span>
      <span></span><span>63450 Hanau</span>
    </div>
    <div class="details__col details__col--web">
      <svg viewBox="0 0 24 24"><circle cx="12" cy="12" r="10" fill="none" stroke="#d9b44a" stroke-width="2"/><path d="M2 12h20M12 2v20M5 6h14M5 18h14" stroke="#d9b44a" stroke-width="1.5" fill="none"/></svg><span>www.feinglanz-hanau.de</span>
      <svg viewBox="0 0 24 24"><path d="M2 5h20v14H2z"/></svg><span>info@feinglanz-hanau.de</span>
    </div>
    <div class="details__col">
      <svg viewBox="0 0 24 24"><path d="M6.6 2.5l3 4-2 2.5c1.2 2.8 3.5 5.5 6.4 7l2.5-2 4 3-2 4.5C10 21 3 14 2.5 4.5z"/></svg><span>Tel.: 06181-5550142</span>
      <svg viewBox="0 0 24 24"><path d="M6 2h10v6H6zM2 9h20v12H2z"/></svg><span>Fax: 06181-5550143</span>
    </div>
  </div>
  <div class="gold-band gold-band--bottom"></div>
</section>

</body>
</html>
```